'Cradle Ahead' promotional brochure

We have designed a 6 week program to educate impending first-time parents about the things they need to know to survive the first 6 months. Sessions delivered by general practitioner/family doctor, dietician, physiotherapist, speech pathologist and psychologist. Our promotional blurb is: 'A comprehensive education program for first-time parents-to-be, delivered over 6 weeks by health professionals in your community, about everything you need to know to look after your baby (and yourself!) in the first 6 months'. I now want to put together a promotional brochure to be distributed to those couples who express an interest which will provide further details of what will be delivered in the course.
Updates
In terms of layout, I envisaged a double sided A4 size, foldable into 3 sections, but very happy to be guided on this.
Target Market(s)
To appeal to a young, well educated demographic. First time parents couples.
Industry/Entity Type
Medical
Font styles to use
Other font styles liked:
- Playfair Display
Requirements
Must have
- Playfair display font to be consistent with our logo (attached). Logo also included please. Some consistency with colours of logo please.
Nice to have
- I am a doctor, and have no creative genes! But prefer a clean and professional appearance overall. Not too cluttered in overall appearance.
Should not have
- No cheesy pictures of babies.

```html
<!DOCTYPE html>
<html lang="en">
<head>
<meta charset="utf-8">
<title>Cradle Ahead – Brochure</title>
<link href="https://fonts.googleapis.com/css2?family=Playfair+Display:wght@400;700&family=Lato:wght@300;400;700&family=Oswald:wght@600&family=Crimson+Text:wght@400;600&family=Orbitron:wght@600&display=swap" rel="stylesheet">
<style>
:root{
  --green:#6bbf45;
  --green-dark:#2f5d3a;
  --charcoal:#4a4a4a;
  --backdrop:#3b3b3b;
  --ink:#333;
  --white:#fff;
  --frame:#b9e29f;
}
*{box-sizing:border-box;margin:0;padding:0}
html,body{width:1200px;height:838px;overflow:hidden;background:var(--backdrop)}
.page{position:absolute;top:42px;width:540px;height:758px;background:var(--white);overflow:hidden;box-shadow:0 2px 8px rgba(0,0,0,.5)}
.page--front{left:32px}
.page--back{left:606px}
.abs{position:absolute}
.brand{font-family:'Playfair Display',serif;font-weight:400;color:var(--green);white-space:nowrap}
.brand--front{font-size:19px;line-height:26px}
.brand--back{font-size:15px;line-height:21px}
.brand-square{background:var(--green)}
.photo{position:absolute}
.side{position:absolute;left:310px;top:0;width:230px;height:758px;background:var(--green)}
.lead{font-family:Lato,sans-serif;font-weight:300;color:var(--white)}
.title{font-family:'Playfair Display',serif;font-weight:700;letter-spacing:1px;white-space:nowrap}
.week-bar{position:absolute;height:23px;width:200px}
.week-label{position:absolute;top:2px;font-family:'Playfair Display',serif;font-size:14px;line-height:18px;color:var(--white);white-space:nowrap}
.body-copy{font-family:'Crimson Text',serif;font-size:8.6px;line-height:11.6px;color:var(--ink);text-align:justify}
.body-copy p+p{margin-top:6px}
.ticks{list-style:none;margin-top:6px}
.ticks li{position:relative;padding-left:12px;line-height:14px;font-size:8.8px}
.ticks li::before{content:"";position:absolute;left:1px;top:3px;width:3px;height:6px;border:solid var(--green);border-width:0 1.5px 1.5px 0;transform:rotate(40deg)}
.on-green{color:var(--white)}
.on-green .ticks li::before{border-color:var(--white)}
.contact{font-family:Lato,sans-serif;color:var(--white);text-align:center}
</style>
</head>
<body>

<section class="page page--front">
  <div class="brand-square abs" style="left:24px;top:40px;width:100px;height:100px"></div>
  <div class="brand brand--front abs" style="left:144px;top:46px">WATTLEBROOK<br>HEALTH &amp;<br>MEDICAL</div>

  <div class="photo" role="img" aria-label="Photo of an expectant mother holding her pregnant belly" style="left:0;top:170px;width:258px;height:284px;background:linear-gradient(100deg,#e9e9e9 0%,#bdb7b2 45%,#9c9590 75%,#d8d4d0 100%)"></div>

  <div class="side"></div>
  <svg class="abs" style="left:230px;top:300px" width="90" height="200" viewBox="0 0 90 200">
    <path d="M90 0 C20 10 0 50 0 100 C0 150 20 190 90 200 Z" fill="#6bbf45"/>
  </svg>

  <div class="lead abs" style="left:330px;top:30px;font-size:26px;line-height:30px">A comprehensive<br>education<br>program for<br>first-time parents</div>
  <div class="lead abs" style="left:330px;top:164px;font-size:16px;line-height:19px;font-weight:400">-to-be, delivered over 6<br>weeks by health<br>professionals in your<br>community, <span style="font-size:13px">about everything<br>you need to know to look after<br>your baby (and yourself!)</span><br>in the first 6 months</div>

  <div class="title abs on-green" style="left:262px;top:322px;font-size:40px">Cradle Ahead</div>
  <div class="abs" style="left:264px;top:377px;font-family:Lato,sans-serif;font-size:10.5px;color:var(--white);white-space:nowrap">Information to be included on promotional brochure</div>

  <div class="abs" style="left:310px;top:452px;width:230px;text-align:center;font-family:Oswald,sans-serif;font-weight:600;font-size:24px;color:var(--white)">TOTAL COST: $300</div>

  <div class="contact abs" style="left:310px;top:520px;width:230px;font-size:19px;line-height:26px;font-weight:300">CONTACT DETAILS<br>FOR ENQUIRIES/<br>BOOKINGS</div>
  <div class="contact abs" style="left:310px;top:612px;width:230px;font-size:29px;font-weight:400">(02)5550 1846</div>
  <div class="contact abs" style="left:310px;top:668px;width:230px;font-size:8.6px;line-height:12.5px;font-weight:700;color:#1f3b1a">Wattlebrook Village, Shop 7, 219<br>Banksia Parade, Wattlebrook NSW 2999.<br>Fax: 02 5550 1847</div>
  <div class="contact abs" style="left:310px;top:707px;width:230px;font-size:8px;color:#1f3b1a">Email: hello@wattlebrookhealth.example</div>
  <div class="contact abs" style="left:310px;top:722px;width:230px;font-size:13px">WattlebrookHealth.example</div>

  <svg class="week-bar" style="left:0;top:444px" width="205" height="23"><polygon points="0,0 200,0 186,23 0,23" fill="#6bbf45"/><polygon points="200,0 205,10 192,10" fill="#2f5d3a"/></svg>
  <div class="week-label" style="left:29px;top:446px">Week 1</div>
  <div class="body-copy abs" style="left:29px;top:472px;width:240px;text-align:left">
    <p>GP Dr Hanna Whitlow will share information for<br>Mum's own health after delivery. Topics include:</p>
    <ul class="ticks">
      <li>Vaccinations in pregnancy</li>
      <li>Bleeding, bladder and bowel after delivery</li>
      <li>Breastfeeding, engorgement and mastitis</li>
      <li>Bottle feeding</li>
      <li>Post-natal anxiety &amp; depression</li>
      <li>Intimacy and contraception</li>
    </ul>
  </div>

  <svg class="week-bar" style="left:0;top:590px" width="205" height="23"><polygon points="0,0 200,0 186,23 0,23" fill="#6bbf45"/><polygon points="200,0 205,10 192,10" fill="#2f5d3a"/></svg>
  <div class="week-label" style="left:29px;top:592px">Week 2</div>
  <div class="body-copy abs" style="left:29px;top:618px;width:266px">
    <p>Session 1 –Clinical Psychologist Dr Simone Arkwright will discuss changes in relationships as couples becomes parents, gender roles in parenting and post-natal depression.</p>
    <p>Session 2 – Physiotherapist Tessa Bramwell will present advice for Mums regarding exercise during and after pregnancy, looking after the pelvic floor during and after pregnancy, and abdominal muscle separation management. She will also provide advice for promoting babies' neck strength and minimising the risk of flat spots on the head and encouraging gross motor skills in the first 6 months</p>
  </div>
</section>

<section class="page page--back">
  <div class="abs" style="left:0;top:0;width:540px;height:339px;background:var(--green)"></div>

  <svg class="week-bar" style="left:0;top:30px" width="205" height="23"><polygon points="0,0 200,0 186,23 0,23" fill="#4a4a4a"/><polygon points="200,0 205,10 192,10" fill="#222"/></svg>
  <div class="week-label" style="left:24px;top:32px">Week 3</div>
  <div class="body-copy abs on-green" style="left:24px;top:60px;width:221px">
    <p>Session 1 – Dietician Maree Tolland provides advice for Mums regarding healthy eating during pregnancy and lactation, normal weight gain during pregnancy and realistic weight loss after. She will also discuss the evidence regarding breastfeeding VS bottle-feeding, normal infant weight gain and introducing solids (including those with potential for allergy).</p>
    <p>Session 2 –Paediatric Speech Pathologist Ruth Calder will share information about latching and breast-feeding troubles &amp; tongue tie, advice about dummies and finger-sucking, introducing solids &amp; feeding (including 'pouch' food), encouraging language development and current evidence about electronic devices impacting language development.</p>
  </div>

  <svg class="week-bar" style="left:0;top:242px" width="205" height="23"><polygon points="0,0 200,0 186,23 0,23" fill="#4a4a4a"/><polygon points="200,0 205,10 192,10" fill="#222"/></svg>
  <div class="week-label" style="left:24px;top:244px">Week 5</div>
  <div class="body-copy abs on-green" style="left:24px;top:272px;width:221px">
    <p>Session 1 –Clinical Psychologist Dr Simone Arkwright will share information about bonding &amp; attachment with your baby, how to promote their social &amp; emotional development and how to manage separation anxiety. She will also discuss positive parenting approaches.</p>
  </div>

  <svg class="week-bar" style="left:260px;top:30px" width="190" height="23"><polygon points="0,0 186,0 172,23 0,23" fill="#4a4a4a"/><polygon points="186,0 190,10 178,10" fill="#222"/></svg>
  <div class="week-label" style="left:272px;top:32px">Week 4</div>
  <div class="body-copy abs on-green" style="left:272px;top:60px;width:250px;text-align:left">
    <p>GP Dr Hanna Whitlow will share advice about your<br>babies' health in the first 6 months, including:</p>
    <ul class="ticks">
      <li>Skin of newborns</li>
      <li>Sleeping</li>
      <li>Crying</li>
      <li>Immunisations</li>
      <li>Fever and infections</li>
      <li>Diarrhoea and constipation</li>
      <li>Teething</li>
      <li>Understanding a baby's signals</li>
    </ul>
  </div>

  <svg class="week-bar" style="left:260px;top:208px" width="190" height="23"><polygon points="0,0 186,0 172,23 0,23" fill="#4a4a4a"/><polygon points="186,0 190,10 178,10" fill="#222"/></svg>
  <div class="week-label" style="left:272px;top:210px">Week 6</div>
  <div class="body-copy abs on-green" style="left:272px;top:238px;width:250px">
    <p>Session 1 – Secret Men's Business – a men-only session (including beer!) with a new father for frank discussion about the road ahead. Mums will do a shopping excursion with the GP &amp; Dietician to Freshway to look at baby products and food – the good and the bad!</p>
    <p>Session 2 - Program review, reflection and evaluation and future session planning when baby is 6 months of age.</p>
  </div>

  <div class="abs" style="left:20px;top:354px;width:280px;height:110px;border:1px solid var(--frame)"></div>
  <div class="abs" style="left:24px;top:358px;width:253px;height:103px;background:var(--charcoal);padding:10px 12px">
    <div style="font-family:Orbitron,sans-serif;font-weight:600;font-size:15.5px;color:var(--green);letter-spacing:.5px;white-space:nowrap">Sessions delivered by:</div>
    <div style="font-family:Lato,sans-serif;font-weight:300;font-size:13.5px;line-height:18.5px;color:var(--white);margin-top:9px;white-space:nowrap">General Practitioner/family doctor,<br>Dietician, Physiotherapist,<br>Speech Pathologist and Psychologist.</div>
  </div>

  <div class="brand-square abs" style="left:306px;top:368px;width:76px;height:76px"></div>
  <div class="brand brand--back abs" style="left:396px;top:374px">WATTLEBROOK<br>HEALTH &amp;<br>MEDICAL</div>

  <div class="photo" role="img" aria-label="Photo of a smiling mother hugging her baby" style="left:24px;top:474px;width:262px;height:284px;background:linear-gradient(120deg,#f3f1ef 0%,#c9a89a 40%,#6d4a3c 60%,#efe9e4 100%)"></div>

  <div class="abs" style="left:300px;top:460px;width:220px;text-align:center;font-family:Lato,sans-serif;font-weight:300;font-size:21px;line-height:28.2px;color:var(--ink)">A comprehensive education program for first-time parents -to-be, delivered over 6 weeks by health professionals in your community,</div>

  <div class="brand-square abs" style="left:246px;top:666px;width:26px;height:26px"></div>
  <div class="title abs" style="left:302px;top:658px;font-size:32px;color:var(--green)">Cradle Ahead</div>
  <div class="abs" style="left:300px;top:712px;width:220px;text-align:right;font-family:'Playfair Display',serif;font-weight:700;font-size:10px;color:var(--ink)">www.WattlebrookHealth.example</div>
</section>

</body>
</html>
```